Keelby marketing postcards (6x9)

I would like to replicate this 6x9 postcard, but update name/logo, phone number, web address, etc. I also need to create a second postcard copying this basic design, but with updated content and background pictures. Updated contact info to be used for both postcards:
Website: www.keelbyhomestay.com
Name: Mark Tessler
Email: mtessler@keelbyhomestay.com
Phone: (555) 246-8130

Requirements
Must have
• Need two 6x9 postcard designs; 1 themed for Rivenport College, 1 for Calder State. Have uploaded photos that can be used in design. RC can be used for RC postcard (only), CS can be used for CS (only), Generic can be used for either. I've tried to upload extra photos so that you can use your creativity in selecting those that work best in the design.
Nice to have
• In the "Color palette" file, it has the two color schemes -- one for Rivenport College and one for Calder State. Those respective color schemes should be heavily represented in each design. Then there are different groups of pictures labelled either "CS" or "RC", plus some labelled "Generic". The generic ones can be used in either design, the others should be used only for the design for that school.

```html
<!DOCTYPE html>
<html lang="en">
<head>
<meta charset="utf-8">
<title>Keelby Homestay Postcard</title>
<link rel="stylesheet" href="https://fonts.googleapis.com/css2?family=Open+Sans:wght@400;600;700&display=swap">
<style>
  :root {
    --page: #e6e6e6;
    --ink: #141414;
    --white: #ffffff;
    --tan-light: #cdb594;
    --tan: #b1946d;
    --tan-dark: #8e6f4a;
    --cream: #fdf6ec;
    --dark: #161616;
    --dark-mid: #3a3a3a;
    --muted: #7d6f61;
    --pill: #d8c6a6;
  }
  * { box-sizing: border-box; margin: 0; padding: 0; }
  html, body { width: 1022px; height: 1200px; overflow: hidden; }
  body {
    background: var(--page);
    font-family: "Open Sans", Arial, sans-serif;
    color: var(--ink);
    position: relative;
  }
  .card {
    position: absolute;
    width: 731px;
    height: 488px;
    left: 146px;
    overflow: hidden;
    box-shadow: 4px 6px 12px rgba(0,0,0,.35);
  }
  .card--front { top: 100px; background: var(--dark); }
  .card--back { top: 637px; background: var(--white); }

  /* Front */
  .front__header {
    position: absolute; left: 0; top: 0; width: 100%; height: 63px;
    background: radial-gradient(ellipse at 30% 0%, #5a5a5a, var(--dark) 70%);
  }
  .front__photo {
    position: absolute; left: 12px; top: 66px; width: 719px; height: 364px;
    background: linear-gradient(180deg, #3c3f5a 0%, #c46a4e 30%, #e59a68 40%, #3b3350 58%, #151620 100%);
  }
  .front__footer {
    position: absolute; left: 0; top: 434px; width: 100%; height: 54px;
    background: linear-gradient(180deg, #2a2a2a, var(--dark));
  }
  .front__panel {
    position: absolute; left: 12px; top: 0; width: 228px; height: 488px;
    background: linear-gradient(180deg, var(--tan-light) 0%, var(--tan) 45%, var(--tan-dark) 100%);
    box-shadow: 4px 0 10px rgba(0,0,0,.4);
    padding: 94px 0 0 14px;
  }
  .front__headline { font-size: 25px; font-weight: 700; line-height: 1.3; color: var(--ink); }
  .rule { width: 106px; height: 2px; background: var(--ink); }
  .front__panel .rule { margin: 14px 0 16px; }
  .front__body { font-size: 15.5px; line-height: 1.45; color: var(--ink); width: 190px; }
  .front__cta { margin: 30px 0 0; width: 200px; text-align: center; font-size: 13px; color: var(--white); }
  .phone-pill {
    display: flex; align-items: center; gap: 12px;
    margin-top: 8px; margin-left: -2px; width: 206px; height: 29px; border-radius: 15px;
    background: linear-gradient(180deg, #3a3a3a, #0e0e0e);
    color: var(--white); font-size: 15px; font-weight: 600; padding-left: 22px;
  }
  .front__name { margin-top: 11px; width: 200px; text-align: center; font-size: 20px; color: var(--cream); }
  .brand {
    position: absolute; display: flex; align-items: center; gap: 8px;
    font-size: 15px; font-weight: 700; letter-spacing: .5px; text-transform: uppercase;
  }
  .brand__mark { width: 14px; height: 14px; }
  .front__brand { right: 14px; top: 20px; color: var(--white); }
  .front__brand .brand__mark { background: var(--white); }
  .front__contacts {
    position: absolute; left: 250px; top: 453px; display: flex; gap: 22px;
    font-size: 13px; font-weight: 600; color: var(--white);
  }
  .contact { display: flex; align-items: center; gap: 6px; }
  .icon { width: 13px; height: 13px; flex: none; }

  /* Back */
  .back__photo-student {
    position: absolute; left: 0; top: 0; width: 135px; height: 113px;
    background: linear-gradient(160deg, #d9dce0, #7f95b4 55%, #2f3a4d);
  }
  .back__photo-tower {
    position: absolute; left: 135px; top: 0; width: 230px; height: 113px;
    background: linear-gradient(180deg, #5f84c0 0%, #a8bcd8 45%, #cfc2ad 60%, #a99a86 100%);
  }
  .back__message {
    position: absolute; left: 0; top: 113px; width: 365px; height: 375px; background: var(--cream);
  }
  .back__band {
    position: absolute; left: 0; top: 115px; width: 373px; height: 120px;
    background: linear-gradient(180deg, var(--tan-light), var(--tan) 50%, var(--tan-dark));
    box-shadow: 0 4px 8px rgba(0,0,0,.3);
    padding: 18px 0 0 26px;
  }
  .back__headline { font-size: 20.5px; font-weight: 700; line-height: 1.4; color: var(--ink); }
  .back__headline em { font-style: normal; color: var(--cream); font-size: 21.5px; }
  .back__text { position: absolute; left: 25px; top: 252px; width: 330px; }
  .back__lead { font-size: 16px; line-height: 1.45; }
  .back__text .rule { margin: 16px 0 10px; }
  .back__note { font-size: 13px; font-weight: 700; line-height: 1.3; color: var(--muted); width: 280px; }
  .back__contact-line {
    display: flex; align-items: center; gap: 10px; margin-top: 18px; font-size: 11.5px;
  }
  .back__contact-line .contact { font-weight: 600; }
  .back__footer {
    position: absolute; left: 0; top: 434px; width: 365px; height: 54px;
    background: linear-gradient(180deg, #3c3c3c, var(--dark));
  }
  .back__url {
    position: absolute; left: 0; top: 459px; width: 365px; text-align: center;
    font-size: 13px; font-weight: 600; color: var(--white);
  }
  .name-pill {
    position: absolute; left: 30px; top: 423px; width: 316px; height: 29px; border-radius: 15px;
    background: var(--pill); box-shadow: 0 2px 4px rgba(0,0,0,.35);
    display: flex; align-items: center; justify-content: center; gap: 10px;
    font-size: 18px; color: var(--ink);
  }
  .name-pill__phone { display: flex; align-items: center; gap: 6px; font-size: 15px; font-weight: 600; }
  .back__brand { left: 372px; top: 36px; color: var(--ink); }
  .back__brand .brand__mark { background: var(--ink); }
  .stamp-box {
    position: absolute; left: 618px; top: 26px; width: 95px; height: 87px;
    border: 1px solid #d6d6d6;
  }
</style>
</head>
<body>

<section class="card card--front">
  <div class="front__header"></div>
  <div class="front__photo" role="img" aria-label="Campus clock tower lit at dusk against an orange sunset sky, with city lights below"></div>
  <div class="front__footer"></div>

  <div class="brand front__brand"><span class="brand__mark"></span>Keelby Homestay</div>

  <div class="front__panel">
    <h1 class="front__headline">Let us help you<br>save thousands<br>on tution costs</h1>
    <div class="rule"></div>
    <p class="front__body">We have been helping out-of-state families gain Texas residency for over 14 years.</p>
    <p class="front__cta">LET US HELP YOU TOO.</p>
    <div class="phone-pill">
      <svg class="icon" viewBox="0 0 16 16" fill="none" stroke="currentColor" stroke-width="1.4"><circle cx="8" cy="8" r="7"/><path d="M5.5 4.5l1.3 1.6-.8 1a5 5 0 0 0 2.9 2.9l1-.8 1.6 1.3-.7 1.2c-3 0-6.4-3.4-6.4-6.4z" fill="currentColor" stroke="none"/></svg>
      (555) 246-8130
    </div>
    <p class="front__name">Mark Tessler</p>
  </div>

  <div class="front__contacts">
    <span class="contact">
      <svg class="icon" viewBox="0 0 16 16"><circle cx="8" cy="8" r="8" fill="#888"/><rect x="4" y="5" width="8" height="6" fill="#222"/></svg>
      mtessler@keelbyhomestay.com
    </span>
    <span class="contact">
      <svg class="icon" viewBox="0 0 16 16" fill="none" stroke="#999" stroke-width="1.3"><circle cx="8" cy="8" r="7"/><circle cx="8" cy="8" r="3"/></svg>
      www.keelbyhomestay.com
    </span>
  </div>
</section>

<section class="card card--back">
  <div class="back__message"></div>
  <div class="back__photo-student" role="img" aria-label="Student in a denim jacket carrying books and a backpack"></div>
  <div class="back__photo-tower" role="img" aria-label="Water tower reading Welcome to Calder Country against a blue sky"></div>

  <div class="back__band">
    <h2 class="back__headline">Calder parents, did you know<br>you can <em>SAVE OVER $13,800</em><br>a semester in tuition?</h2>
  </div>

  <div class="back__text">
    <p class="back__lead">Establishing Texas residency throught a property purchase is as easy as 1-2-3.</p>
    <div class="rule"></div>
    <p class="back__note">Contact us to learn how we have helped more than 500 families - and counting save thousands on tution.</p>
    <div class="back__contact-line">
      <span>Let us help you too.</span>
      <span class="contact">
        <svg class="icon" viewBox="0 0 16 16"><circle cx="8" cy="8" r="8" fill="#888"/><rect x="4" y="5" width="8" height="6" fill="#fff"/></svg>
        mtessler@keelbyhomestay.com
      </span>
    </div>
  </div>

  <div class="back__footer"></div>
  <p class="back__url">www.keelbyhomestay.com</p>

  <div class="name-pill">
    <span>Mark Tessler</span>
    <span class="name-pill__phone">
      <svg class="icon" viewBox="0 0 16 16" fill="none" stroke="currentColor" stroke-width="1.4"><circle cx="8" cy="8" r="7"/><path d="M5.5 4.5l1.3 1.6-.8 1a5 5 0 0 0 2.9 2.9l1-.8 1.6 1.3-.7 1.2c-3 0-6.4-3.4-6.4-6.4z" fill="currentColor" stroke="none"/></svg>
      (555) 246-8130
    </span>
  </div>

  <div class="brand back__brand"><span class="brand__mark"></span>Keelby Homestay</div>
  <div class="stamp-box"></div>
</section>

</body>
</html>
```